Brochure Design Project

Willow Hearth is a family run all natural residential cleaning company
I am looking for 1 trifold brochure for all clients
I am looking for 2 holiday single sided brochure for deep cleanings and 20% off
(Holiday Ready? Or a Naughty list check list?)
I am looking for a single sided brochure to target specific buildings in SF ( I will change the building name to target). Limitations are that cleanings must be performed on Tuesday or Wednesday with cleaning arrival flexibility
1 single sided brochure for Office/Commercial Cleaning
Target Market(s)
Mom's, pet owners, people with disposable income
Industry/Entity Type
It Company
Font styles to use
Look and feel
Each slider illustrates characteristics of the customer's brand and the style your logo design should communicate.

```html
<!DOCTYPE html>
<html lang="en">
<head>
<meta charset="utf-8">
<title>Willow Hearth – Green Cleaning Flyer</title>
<link href="https://fonts.googleapis.com/css2?family=Josefin+Sans:wght@400;600;700&family=Roboto:ital,wght@0,400;0,500;1,500;1,700&display=swap" rel="stylesheet">
<style>
  :root{
    --backdrop:#000;
    --paper:#ffffff;
    --sky:#1ba6df;
    --band:#19b3e6;
    --leaf:#7ac943;
    --slate:#5f6163;
    --ink:#2e2e2e;
    --muted:#555b60;
    --row-light:#eef6fc;
    --row-dark:#e1edf5;
    --rule:#8e9296;
  }
  *{box-sizing:border-box;margin:0;padding:0}
  html,body{width:967px;height:1200px;overflow:hidden;background:var(--backdrop)}
  .flyer{position:absolute;left:140px;top:102px;width:696px;height:986px;background:var(--paper);overflow:hidden;font-family:"Josefin Sans",sans-serif}
  .shapes{position:absolute;inset:0}
  .headline{position:absolute;left:0;width:490px;top:322px;text-align:center;color:var(--sky);font-weight:700;font-size:31px;line-height:41px;
    text-shadow:0 0 2px #fff,0 0 2px #fff,1px 1px 0 #fff,-1px -1px 0 #fff,1px -1px 0 #fff,-1px 1px 0 #fff,0 0 6px rgba(255,255,255,.8)}
  .intro{position:absolute;left:26px;top:494px;width:218px;color:var(--sky);font-size:20px;line-height:27px}
  .body-copy{position:absolute;left:26px;top:652px;width:226px;color:var(--ink);font-size:15px;line-height:24.5px}
  .price-table{position:absolute;left:230px;top:430px;width:466px;border-collapse:collapse;font-family:"Roboto",sans-serif}
  .price-table th{height:103px;padding-top:48px;color:#fff;font-style:italic;font-weight:700;font-size:15.5px;text-align:center}
  .price-table td{height:38px;font-size:11.5px;color:var(--muted);text-align:center}
  .price-table td.label{text-align:right;padding-right:22px;font-weight:500;color:#3a3d40;width:180px}
  .price-table td.rate{width:143px}
  .brand{position:absolute;left:474px;top:812px;white-space:nowrap;color:#4a4d50;font-weight:600;font-size:21px;letter-spacing:1px}
  .tagline{position:absolute;left:0;width:482px;top:884px;text-align:center;color:#fff;font-size:27px;font-weight:600}
  .tagline small{font-size:22px}
  .contact{position:absolute;top:940px;display:flex;align-items:center;gap:6px;color:#fff;font-size:18px;font-weight:600}
  .contact.phone{left:13px}
  .contact.mail{left:192px}
  .contact.place{left:468px;font-size:15px;line-height:20px}
  .icon{width:32px;height:32px;flex:none}
</style>
</head>
<body>
<div class="flyer">
  <svg class="shapes" viewBox="0 0 696 986" width="696" height="986">
    <defs>
      <linearGradient id="photoTone" x1="0" y1="0" x2="1" y2="1">
        <stop offset="0" stop-color="#f4f8fb"/>
        <stop offset="0.45" stop-color="#c9dce8"/>
        <stop offset="0.75" stop-color="#3f86c4"/>
        <stop offset="1" stop-color="#e7d36a"/>
      </linearGradient>
      <linearGradient id="circleTone" x1="0" y1="0" x2="0" y2="1">
        <stop offset="0" stop-color="#e9eef0"/>
        <stop offset="1" stop-color="#b9c3c6"/>
      </linearGradient>
    </defs>
    <rect class="table-bg" x="410" y="533" width="286" height="370" fill="var(--row-light)"/>
    <rect class="table-head" x="410" y="410" width="286" height="123" fill="var(--slate)"/>
    <path class="hero-photo" role="img" aria-label="Photo of a smiling cleaner in an apron with a colleague wiping surfaces behind her"
      d="M0 0H696V420C600 410 490 420 400 445C300 472 200 474 110 444C66 429 28 414 0 408Z" fill="url(#photoTone)"/>
    <path class="hero-edge" d="M0 408C28 414 66 429 110 444C200 474 300 472 400 445C490 420 600 410 696 420" fill="none" stroke="var(--leaf)" stroke-width="6"/>
    <g class="detail-circles" stroke="#fff" stroke-width="3">
      <circle role="img" aria-label="Photo of a gloved hand wiping with a cloth" cx="566" cy="97" r="69" fill="url(#circleTone)"/>
      <circle role="img" aria-label="Photo of a bright, tidy living room" cx="566" cy="251" r="69" fill="url(#circleTone)"/>
      <circle role="img" aria-label="Photo of a clean modern kitchen" cx="566" cy="403" r="69" fill="url(#circleTone)"/>
    </g>
    <g class="table-stripes" fill="var(--row-dark)">
      <rect x="410" y="577" width="286" height="38"/>
      <rect x="410" y="653" width="286" height="38"/>
      <rect x="410" y="729" width="286" height="38"/>
    </g>
    <path class="footer-rule" d="M0 895C120 846 260 841 380 848C500 854 620 866 696 876" fill="none" stroke="var(--rule)" stroke-width="5"/>
    <path class="footer-band" d="M0 900C120 851 260 846 380 853C500 859 620 871 696 881V986H0Z" fill="var(--band)"/>
  </svg>

  <h1 class="headline">San Francisco Bay's premier<br>green cleaning service.</h1>

  <p class="intro">We deliver a greener, safer clean to your home and your family with our environmentally friendly products.</p>
  <p class="body-copy">We don’t cut corners with the use of harsh chemicals and only use products that are natural, environmentally friendly and safe for your family and pets. It takes a little more effort but we feel you’re worth it!</p>

  <table class="price-table">
    <thead><tr><th></th><th>Regular Cleaning</th><th>Deep Cleaning</th></tr></thead>
    <tbody>
      <tr><td class="label">Kitchen / Bath Only</td><td class="rate">$100</td><td class="rate">$150</td></tr>
      <tr><td class="label">Studio</td><td class="rate">$125</td><td class="rate">$250</td></tr>
      <tr><td class="label">1 Bed / 1 Bath</td><td class="rate">$150</td><td class="rate">$300</td></tr>
      <tr><td class="label">2 Bed / 1 Bath</td><td class="rate">$175 - $200</td><td class="rate">$350 - $400</td></tr>
      <tr><td class="label">2 Bed / 2 Bath</td><td class="rate">$225 - $275</td><td class="rate">$425 - $475</td></tr>
      <tr><td class="label">3 Bed / 2 Bath</td><td class="rate">$300 - $350</td><td class="rate">$500 - $550</td></tr>
      <tr><td class="label">4+ Bed</td><td class="rate">Contact Us</td><td class="rate"></td></tr>
    </tbody>
  </table>

  <div class="brand">Willow Hearth</div>

  <p class="tagline">Live a Cleaner, <small>Greener Life</small></p>

  <div class="contact phone">
    <svg class="icon" viewBox="0 0 32 32"><circle cx="16" cy="16" r="14" fill="none" stroke="#fff" stroke-width="2"/><path d="M11 9l3 0 1.5 4-2 1.5c1 2.2 2.3 3.5 4.5 4.5l1.5-2 4 1.5v3c0 1-1 2-2 2-6.5-.5-11.5-5.5-12-12 0-1 1-2 1.5-2.5z" fill="#fff"/></svg>
    <span>(415) 555-0142</span>
  </div>
  <div class="contact mail">
    <svg class="icon" viewBox="0 0 32 32"><circle cx="16" cy="16" r="14" fill="none" stroke="#fff" stroke-width="2"/><rect x="9" y="11" width="14" height="10" rx="1.5" fill="none" stroke="#fff" stroke-width="1.8"/><path d="M9.5 12l6.5 5 6.5-5" fill="none" stroke="#fff" stroke-width="1.8"/></svg>
    <span>hello@willowhearth.com</span>
  </div>
  <div class="contact place">
    <svg class="icon" viewBox="0 0 32 32"><circle cx="16" cy="16" r="14" fill="none" stroke="#fff" stroke-width="2"/><path d="M16 24s-5.5-6-5.5-9.5a5.5 5.5 0 0 1 11 0C21.5 18 16 24 16 24z" fill="none" stroke="#fff" stroke-width="1.8"/><circle cx="16" cy="14.5" r="2" fill="#fff"/></svg>
    <span>214 Larkin Row, 3rd floor<br>San Francisco CA 94103</span>
  </div>
</div>
</body>
</html>
```